Modern and Improved business card design for Family Dental Practice

We have 2 sets of logo we have designed and now just need a business card layout and design for the office. Colors are on the logo. We can choose which logo we want to go with . The font can be changed to whatever seems modern and relevant. We are family dental office that has been open for over 15 years in South Austin Texas.

Target Market(s)

Handout Business cards to referrals and specialists

Industry/Entity Type

Dental

Contact Information for Business Card

We need address, phone, website and email address. 4870 North Loop Rd Suite 208 , Austin,Texas 78651....phone: 512-480-7319.....email- info@maplebrookdental-example.com....website - MapleBrookDental-example.com

Font styles to use
Serif
Decorative

Requirements
Must have
• my logo. We have 2 logos, but we can use just one or if we can incorporate one on one side and the other on the other side.
Nice to have
• Really just need a modern look and clean that incorporates the logo and colors .

```html
<!DOCTYPE html>
<html lang="en">
<head>
<meta charset="utf-8">
<title>Maple Brook Family Dentistry – Business Card</title>
<link rel="stylesheet" href="https://fonts.googleapis.com/css2?family=Arimo:wght@400&family=Josefin+Sans:wght@300;400&display=swap">
<style>
  :root {
    --backdrop: #2b2b2c;
    --card-white: #ffffff;
    --card-black: #141516;
    --brand-green: #2f8a1c;
    --brand-green-light: #8db83a;
    --ink: #1c1c1c;
    --ink-soft: #2a2a2a;
    --rule: #9a9a9a;
    --on-dark: #f2f2f2;
  }
  * { box-sizing: border-box; margin: 0; padding: 0; }
  html, body {
    width: 1200px; height: 1108px; overflow: hidden;
    background: var(--backdrop);
  }
  .stage {
    position: relative; width: 1200px; height: 1108px;
    display: flex; justify-content: center; align-items: center; gap: 60px;
  }
  .card {
    width: 390px; height: 660px; border-radius: 22px;
    position: relative; overflow: hidden;
    box-shadow: 0 18px 40px rgba(0,0,0,.45);
  }

  /* Front */
  .card-front {
    background: var(--card-white);
    display: flex; flex-direction: column; align-items: center;
    padding-top: 80px;
  }
  .brand {
    display: flex; align-items: center; gap: 22px;
  }
  .brand-dot {
    width: 78px; height: 78px; border-radius: 50%;
    background: var(--brand-green);
    flex: none;
  }
  .brand-name {
    font-family: "Josefin Sans", sans-serif; font-weight: 300;
    font-size: 44px; line-height: .95; color: var(--ink);
    letter-spacing: 1px; text-transform: uppercase;
  }
  .brand-tagline {
    font-family: "Josefin Sans", sans-serif; font-weight: 300;
    font-size: 17px; letter-spacing: 2px; color: var(--brand-green);
    text-transform: uppercase; margin-top: 14px; margin-left: 100px;
  }
  .person {
    margin-top: 70px; text-align: center;
  }
  .person-name {
    font-family: "Josefin Sans", sans-serif; font-weight: 400;
    font-size: 27px; color: var(--brand-green); text-transform: uppercase;
    letter-spacing: .5px;
  }
  .person-role {
    font-family: "Arimo", sans-serif; font-size: 18px; color: var(--ink-soft);
    margin-top: 6px;
  }
  .divider {
    display: flex; align-items: center; gap: 8px;
    width: 300px; margin-top: 18px;
  }
  .divider::before, .divider::after {
    content: ""; flex: 1; height: 1px; background: var(--rule);
  }
  .icon {
    width: 30px; height: 30px; border-radius: 4px;
    background: var(--brand-green); display: flex;
    align-items: center; justify-content: center;
  }
  .icon svg { width: 20px; height: 20px; }
  .contact {
    font-family: "Arimo", sans-serif; font-size: 18px; line-height: 1.35;
    color: var(--ink-soft); text-align: center; margin-top: 12px;
  }
  .contact-email { font-size: 17px; }

  /* Back */
  .card-back { background: var(--card-black); }
  .back-texture {
    position: absolute; inset: 0;
    background: linear-gradient(135deg, #0f1011 0%, #1b1c1e 45%, #3a3b3d 100%);
  }
  .back-brand {
    position: absolute; left: 110px; top: 440px;
    display: flex; align-items: center; gap: 14px;
  }
  .back-brand .brand-dot { width: 40px; height: 40px; }
  .back-brand .brand-name { font-size: 28px; color: var(--on-dark); }
</style>
</head>
<body>
<main class="stage">

  <section class="card card-front" aria-label="Business card front">
    <div class="brand">
      <span class="brand-dot" aria-hidden="true"></span>
      <h1 class="brand-name">Maple<br>Brook</h1>
    </div>
    <p class="brand-tagline">Family Dentistry</p>

    <div class="person">
      <h2 class="person-name">Daniel R Mehta DDS</h2>
      <p class="person-role">Dentist</p>
    </div>

    <div class="divider">
      <span class="icon" aria-label="Phone">
        <svg viewBox="0 0 24 24" fill="none" stroke="#fff" stroke-width="2" stroke-linecap="round" stroke-linejoin="round">
          <path d="M22 16.9v3a2 2 0 0 1-2.2 2 19.8 19.8 0 0 1-8.6-3.1 19.5 19.5 0 0 1-6-6A19.8 19.8 0 0 1 2.1 4.2 2 2 0 0 1 4.1 2h3a2 2 0 0 1 2 1.7c.1.9.4 1.8.7 2.7a2 2 0 0 1-.5 2.1L8 9.8a16 16 0 0 0 6 6l1.3-1.3a2 2 0 0 1 2.1-.4c.9.3 1.8.6 2.7.7a2 2 0 0 1 1.7 2z"/>
        </svg>
      </span>
      <span class="icon" aria-label="Email">
        <svg viewBox="0 0 24 24" fill="none" stroke="#fff" stroke-width="2" stroke-linejoin="round">
          <rect x="3" y="5" width="18" height="14" rx="1"/><path d="M3 6l9 7 9-7"/>
        </svg>
      </span>
      <span class="icon" aria-label="Website">
        <svg viewBox="0 0 24 24" fill="none" stroke="#fff" stroke-width="2">
          <circle cx="12" cy="12" r="9"/><path d="M3 12h18M12 3c3 3 3 15 0 18M12 3c-3 3-3 15 0 18"/>
        </svg>
      </span>
    </div>

    <address class="contact" style="font-style:normal">
      <p>512-480-7319</p>
      <p class="contact-email">info@maplebrookdental-example.com</p>
      <p>MapleBrookDental-example.com</p>
    </address>

    <div class="divider">
      <span class="icon" aria-label="Location">
        <svg viewBox="0 0 24 24" fill="none" stroke="#fff" stroke-width="2">
          <path d="M12 22s7-6.5 7-12a7 7 0 0 0-14 0c0 5.5 7 12 7 12z"/><circle cx="12" cy="10" r="2.5"/>
        </svg>
      </span>
    </div>

    <address class="contact" style="font-style:normal">
      <p>4870 North Loop Rd Suite 208</p>
      <p>Austin, Texas 78651</p>
    </address>
  </section>

  <section class="card card-back" aria-label="Business card back">
    <div class="back-texture" role="img" aria-label="Glossy tone-on-tone repeating brand pattern across the black card"></div>
    <div class="back-brand">
      <span class="brand-dot" aria-hidden="true"></span>
      <p class="brand-name">Maple<br>Brook</p>
    </div>
  </section>

</main>
</body>
</html>
```